Oil and Gas Letterhead Design Tweak

Simple letterhead information and design tweak.

Please note, we don't want to change the design or logo of the letterhead only the small changes mentioned below.

We need to change the company name up top to "Northvale Petrotek FZCO"

Also, we need to include in the footer the following information. I have attached an image of roughly how we would like to have it displayed in the footer.

Footer Details:

Northvale Petrotek FZCO,
Unit No. 2378, FZCO Trade Hub, level No. 1, K&P 7, Dubai, United Arab Emirates
Northvale Petrotek FZCO is registered as a free zone company under the rules & regulations of FZCO

Target Market(s)

O&G Market

Industry/Entity Type

Oil And Gas

Font styles to use
Sans Serif

Colors

Designer to choose colors to be used in the design.

Requirements
Must have
• Change the company name to Northvale Petrotek FZCO
• Include the footer on the bottom of the first and continuation page
Should not have
• Should not change the design or logo of the letterhead, only the specified changes mentioned above

```html
<!DOCTYPE html>
<html lang="en">
<head>
<meta charset="utf-8">
<title>Northvale Petrotek FZCO — Letterhead</title>
<link href="https://fonts.googleapis.com/css2?family=Open+Sans:wght@400;600;700&display=swap" rel="stylesheet">
<style>
  :root {
    --bg: #e9eaec;
    --paper: #ffffff;
    --brand-blue: #2a4fa8;
    --brand-red: #e0262b;
    --ink: #2b2f36;
    --ink-soft: #555b64;
  }
  * { box-sizing: border-box; margin: 0; padding: 0; }
  html, body { width: 1200px; height: 848px; overflow: hidden; }
  body {
    background: var(--bg);
    font-family: "Open Sans", Arial, sans-serif;
    color: var(--ink);
    position: relative;
  }
  .sheet {
    position: absolute;
    top: 44px;
    width: 537px;
    height: 760px;
    background: var(--paper);
    box-shadow: 0 2px 10px rgba(0,0,0,.08);
    overflow: hidden;
  }
  .sheet--first { left: 45px; }
  .sheet--continuation { left: 618px; }

  /* first page header */
  .header-rule { position: absolute; top: 0; left: 0; width: 100%; height: 6px; }
  .brand {
    position: absolute;
    display: flex;
    align-items: center;
    gap: 7px;
    font-weight: 600;
    color: var(--brand-blue);
    white-space: nowrap;
  }
  .brand__mark { width: 12px; height: 12px; background: var(--brand-red); }
  .sheet--first .brand { top: 18px; left: 28px; font-size: 13px; }

  /* footer block */
  .footer {
    position: absolute;
    left: 28px;
    bottom: 42px;
    font-size: 7.2px;
    line-height: 1.55;
    letter-spacing: .03em;
    text-transform: uppercase;
  }
  .footer__name { font-weight: 700; color: var(--ink); text-align: center; }
  .footer__address { font-weight: 600; color: var(--ink); }
  .footer__legal { font-weight: 400; color: var(--ink-soft); font-size: 6.4px; }

  .corner-tabs { position: absolute; width: 40px; height: 10px; }
  .sheet--first .corner-tabs { right: 26px; bottom: 22px; }
  .sheet--continuation .corner-tabs { right: 0; top: 110px; }

  /* continuation page */
  .sheet--continuation .footer { bottom: 76px; }
  .base-band { position: absolute; left: 0; bottom: 24px; width: 100%; height: 14px; }
  .sheet--continuation .brand { right: 14px; bottom: 8px; font-size: 9px; }
</style>
</head>
<body>

  <section class="sheet sheet--first" aria-label="First page letterhead">
    <svg class="header-rule" viewBox="0 0 537 6" preserveAspectRatio="none">
      <rect x="0" y="0" width="140" height="6" fill="var(--brand-blue)"/>
      <polygon points="140,0 537,0 537,6 146,6" fill="var(--brand-red)"/>
      <polygon points="136,0 142,0 148,6 142,6" fill="#fff"/>
    </svg>
    <div class="brand"><span class="brand__mark"></span>Northvale Petrotek FZCO</div>

    <footer class="footer">
      <p class="footer__name">Northvale Petrotek FZCO</p>
      <p class="footer__address">Unit No. 2378 | FZCO Trade Hub | Level No. 1, K&amp;P 7 | Dubai | United Arab Emirates</p>
      <p class="footer__legal">Northvale Petrotek FZCO is registered as a free zone company under the rules &amp; regulations of FZCO</p>
    </footer>
    <svg class="corner-tabs" viewBox="0 0 40 10">
      <polygon points="0,0 16,0 20,10 4,10" fill="var(--brand-blue)"/>
      <polygon points="21,0 36,0 40,10 25,10" fill="var(--brand-red)"/>
    </svg>
  </section>

  <section class="sheet sheet--continuation" aria-label="Continuation page letterhead">
    <svg class="corner-tabs" viewBox="0 0 40 10">
      <polygon points="0,0 18,0 22,10 4,10" fill="var(--brand-blue)"/>
      <polygon points="23,0 40,0 40,10 27,10" fill="var(--brand-red)"/>
    </svg>

    <footer class="footer">
      <p class="footer__name">Northvale Petrotek FZCO</p>
      <p class="footer__address">Unit No. 2378 | FZCO Trade Hub | Level No. 1, K&amp;P 7 | Dubai | United Arab Emirates</p>
      <p class="footer__legal">Northvale Petrotek FZCO is registered as a free zone company under the rules &amp; regulations of FZCO</p>
    </footer>

    <svg class="base-band" viewBox="0 0 537 14" preserveAspectRatio="none">
      <polygon points="0,0 360,0 374,14 0,14" fill="var(--brand-blue)"/>
      <polygon points="366,0 372,0 386,14 380,14" fill="var(--brand-blue)"/>
    </svg>
    <div class="brand"><span class="brand__mark"></span>Northvale Petrotek FZCO</div>
  </section>

</body>
</html>
```